Flyer Design for Exciting Fundraising Personalised Medal Hangers

We are a small Aussie business, Plaquora, who are interested in having a colourful flyer designed to promote our personalised medal hangers. We wish to show a quality product which will be fun and exciting for club members. People should be proud to display their hard earned awards.

Business information:
Plaquora
(07) 4913 2576
info@Plaquora.com.au
www.Plaquora.com.au

Target Market(s)

Mums, sports clubs, dance clubs

Industry/Entity Type

Club

Requirements
Must have
• Fundraiser
• Unique
• Personalised
• 25% of proceeds to your club
• From just $30
• Choice of Size
• Choice of Colour
• Choice of Images
• Add Extensions
• Traditional fundraiser or Easy Online order
• Images attached of 'Medal Hanger Double/Triple/Quadruple' can be used if possible. Even if just 1 of the 3 images are used to show we can add extensions.
Nice to have
• I'd just like something colourful and eye catching. Do you have your own sporting medals? Would you like a fun and colourful personalised way to display them?

```html
<!DOCTYPE html>
<html lang="en">
<head>
<meta charset="utf-8">
<title>Plaquora Medal Hanger Fundraiser Flyer</title>
<link rel="stylesheet" href="https://fonts.googleapis.com/css2?family=Cinzel:wght@600&family=Cormorant+Garamond:ital,wght@0,500;0,600;1,500&family=Open+Sans:wght@700&display=swap">
<style>
  :root {
    --backdrop: #71838a;
    --sun-yellow: #ffff55;
    --lilac: #e8b8e2;
    --edge-white: #ffffff;
    --leaf-green: #2a9a1a;
    --copy-green: #1f8a1f;
    --ink: #111111;
    --offer-red: #cc1111;
    --star-light: #fffa9a;
    --star-deep: #e6d640;
    --arrow-fill: #fbfbc4;
  }
  * { margin: 0; padding: 0; box-sizing: border-box; }
  html, body { width: 1200px; height: 1000px; overflow: hidden; background: var(--backdrop); }
  .flyer { position: absolute; left: 245px; top: 0; width: 710px; height: 1000px; background: var(--lilac); overflow: hidden; }
  .flyer-bands { position: absolute; inset: 0; }
  .brand { position: absolute; left: 0; top: 58px; width: 710px; text-align: center;
    font-family: "Cormorant Garamond", serif; font-weight: 600; font-size: 50px; line-height: 60px; color: var(--ink); }
  .title { position: absolute; left: 0; width: 710px; text-align: center; color: var(--leaf-green); line-height: 1; }
  .title-main { top: 170px; font-family: "Cinzel", serif; font-weight: 600; font-size: 52px; letter-spacing: 1px; }
  .title-sub { top: 240px; font-family: "Cormorant Garamond", serif; font-style: italic; font-weight: 500; font-size: 56px; }
  .product-shot { position: absolute; left: 40px; top: 355px; width: 318px; height: 430px; border-radius: 6px;
    background: linear-gradient(180deg, #a4264f 0%, #a4264f 20%, #6a5a8a 45%, #7a6a78 75%, #6a5048 100%); opacity: 0.85; }
  .offer-star { position: absolute; left: 0; top: 0; width: 710px; height: 1000px; }
  .offer { position: absolute; left: 385px; top: 425px; width: 270px; text-align: center; color: var(--offer-red); transform: rotate(-20deg); }
  .offer-figure { font-family: "Cormorant Garamond", serif; font-weight: 500; font-size: 92px; line-height: 0.95; }
  .offer-note { font-family: "Cormorant Garamond", serif; font-style: italic; font-weight: 500; font-size: 42px; line-height: 1.05; }
  .tagline { position: absolute; left: 80px; top: 848px; width: 550px; text-align: center; font-family: "Open Sans", sans-serif; font-weight: 700; font-size: 27px; line-height: 36px; color: var(--copy-green); }
  .next-arrow { position: absolute; left: 625px; top: 932px; width: 52px; height: 36px; }
</style>
</head>
<body>
<main class="flyer">
  <svg class="flyer-bands" viewBox="0 0 710 1000" aria-hidden="true">
    <path d="M0 0 H710 V240 Q355 400 0 240 Z" fill="var(--sun-yellow)"/>
    <path d="M710 240 Q355 400 0 240" fill="none" stroke="var(--edge-white)" stroke-width="6"/>
    <path d="M0 885 Q355 710 710 885 V1000 H0 Z" fill="var(--sun-yellow)"/>
    <path d="M0 885 Q355 710 710 885" fill="none" stroke="var(--edge-white)" stroke-width="6"/>
  </svg>

  <div class="brand">Plaquora</div>

  <h1 class="title title-main">Medal Hanger</h1>
  <p class="title title-sub">Fundraiser</p>

  <div class="product-shot" role="img" aria-label="Personalised medal hanger with name plate and medals hanging on coloured ribbons"></div>

  <svg class="offer-star" viewBox="0 0 710 1000" aria-hidden="true">
    <defs>
      <linearGradient id="starFill" x1="0" y1="0" x2="0" y2="1">
        <stop offset="0" stop-color="var(--star-light)"/>
        <stop offset="1" stop-color="var(--star-deep)"/>
      </linearGradient>
      <filter id="starShadow" x="-20%" y="-20%" width="140%" height="140%">
        <feDropShadow dx="4" dy="5" stdDeviation="4" flood-color="#000" flood-opacity="0.45"/>
      </filter>
    </defs>
    <polygon filter="url(#starShadow)" fill="url(#starFill)"
      points="515,357 567,408 641,409 642,483 693,535 642,587 641,661 567,662 515,713 463,662 389,661 388,587 337,535 388,483 389,409 463,408"/>
  </svg>

  <div class="offer">
    <div class="offer-figure">25%</div>
    <div class="offer-note">proceeds to<br>your club</div>
  </div>

  <p class="tagline">Unique and exciting fundraiser to<br>proudly display your hard-earned<br>medals</p>

  <svg class="next-arrow" viewBox="0 0 52 36" aria-hidden="true">
    <polygon points="2,11 30,11 30,2 50,18 30,34 30,25 2,25" fill="var(--arrow-fill)" stroke="#333" stroke-width="2" stroke-linejoin="round"/>
  </svg>
</main>
</body>
</html>
```